Tallyleaf Web Design

Create Website Design for Tallyleaf. Tallyleaf is online application for collaboration team work system (task list management). More concept design for this project please find attach file ("tallyleaf website concept.pdf") . But my concept is just describe minimal features not bind design

For tallyleaf logo, i had already attach files. But i had not decided what color i chose, so it's okay if you suggest logo color for your suitable website design.
Updates

Dear All Designer,

I like brisk carousel (http://quorvanlabs.example/brisk-carousel/),
may be your concept design can adjust with this concept.
but don't worry about script for brisk carousel, my team will be handle
You just make website design to suitable with brisk carousel

but if you had own website design concept are welcome

thanks

Target Market(s)

Business Company

Industry/Entity Type

Management

```html
<!DOCTYPE html>
<html lang="en">
<head>
<meta charset="utf-8">
<title>Tallyleaf — Online Collaboration</title>
<link rel="stylesheet" href="https://fonts.googleapis.com/css2?family=Arimo:wght@400&family=Varela+Round&display=swap">
<style>
:root{
  --teal:#214a55;
  --lime:#99c22e;
  --lime-dark:#6a9a22;
  --sky:#29a6c0;
  --ink:#1f1f1f;
  --nav-ink:#1f3f48;
  --panel:#e7e7e7;
  --bar:#0d0d0d;
  --track:#5a5a5a;
  --white:#ffffff;
}
*{box-sizing:border-box;margin:0;padding:0}
html,body{width:1200px;height:921px;overflow:hidden;background:var(--white);font-family:"Arimo",Arial,sans-serif;color:var(--ink)}
a{text-decoration:none;color:inherit}
.brand{position:absolute;left:120px;top:34px;display:flex;align-items:center;gap:12px;font-family:"Varela Round",Arial,sans-serif;font-size:50px;line-height:60px;color:var(--teal);letter-spacing:-1px}
.brand-dot{width:22px;height:22px;border-radius:50%;background:var(--lime)}
.main-nav a{position:absolute;top:54px;height:30px;line-height:30px;font-size:14px;color:var(--nav-ink)}
.main-nav a.active{left:426px;width:52px;text-align:center;background:var(--lime);color:var(--teal)}
.main-nav a.active::after{content:"";position:absolute;left:12px;bottom:-7px;border-left:7px solid var(--lime);border-bottom:7px solid transparent}
.nav-about{left:505px}.nav-features{left:576px}.nav-customers{left:664px}
.nav-tour{left:764px}.nav-solutions{left:826px}.nav-contact{left:917px}
.login{position:absolute;left:1003px;top:54px;width:77px;height:30px;background:var(--lime-dark);color:var(--white);font-size:17px;text-align:center;line-height:30px}
.hero{position:absolute;left:120px;top:130px;width:960px;height:426px}
.video{position:absolute;left:0;top:0;width:613px;height:426px}
.video-frame{position:absolute;inset:0 0 46px 0;background:radial-gradient(ellipse at 55% 45%,#4a5646 0%,#2e3a2e 55%,#1a221a 100%)}
.play-big{position:absolute;left:287px;top:188px;width:40px;height:40px}
.controls{position:absolute;left:0;bottom:0;width:613px;height:46px;background:var(--bar)}
.ctrl-play{position:absolute;left:11px;top:7px;width:32px;height:31px}
.ctrl-track{position:absolute;left:47px;top:7px;width:554px;height:31px;background:var(--track)}
.progress{position:absolute;left:9px;top:11px;width:498px;height:8px;background:#111}
.progress span{display:block;width:228px;height:8px;background:var(--lime)}
.knob{position:absolute;left:230px;top:8px;width:14px;height:14px;border-radius:50%;background:var(--white)}
.time{position:absolute;right:7px;top:8px;font-size:12px;color:var(--white)}
.slide{position:absolute;left:613px;top:0;width:347px;height:426px;background:var(--teal);text-align:center}
.slide-mark{position:absolute;left:162px;top:72px;width:24px;height:24px;border-radius:50%;background:var(--lime)}
.slide-line{position:absolute;left:0;width:100%;font-weight:400;white-space:nowrap}
.l1{top:190px;font-size:60px;line-height:60px;color:var(--lime);letter-spacing:-1px}
.l2{top:252px;font-size:34px;line-height:36px;color:var(--white);letter-spacing:-0.5px}
.l3{top:288px;font-size:54px;line-height:56px;color:var(--sky);letter-spacing:-0.5px}
.dots{position:absolute;left:107px;top:370px;display:flex;gap:4px}
.dots i{width:19px;height:19px;background:var(--lime-dark)}
.dots i.on{background:var(--lime)}
.features{position:absolute;left:120px;top:571px;width:960px;display:flex;gap:15px}
.feature{width:310px;height:249px;background:var(--panel);text-align:center}
.feature h3{font-weight:400;font-size:22px;line-height:26px;margin-top:14px;height:42px;letter-spacing:-0.3px}
.feature .photo{display:block;margin:0 auto;width:274px;height:176px}
.photo-apps{background:linear-gradient(150deg,#7a858e 0%,#4b555d 45%,#2b3238 100%)}
.photo-servers{background:linear-gradient(90deg,#1e232a 0%,#3a424c 35%,#c9ccd1 50%,#3a424c 65%,#1e232a 100%)}
.photo-report{background:linear-gradient(160deg,#f1f2ec 0%,#cfe09a 45%,#5e8f2a 100%)}
.footer-nav{position:absolute;left:0;top:843px;width:1200px;text-align:center;font-size:16px;line-height:20px;word-spacing:0}
.footer-nav a{color:var(--ink);margin:0 9px}
.copyright{position:absolute;left:0;top:880px;width:1200px;text-align:center;font-size:14px}
</style>
</head>
<body>
<header class="site-header">
  <div class="brand"><span>tallyleaf</span><span class="brand-dot"></span></div>
  <nav class="main-nav">
    <a class="active" href="#">Home</a>
    <a class="nav-about" href="#">About</a>
    <a class="nav-features" href="#">Features</a>
    <a class="nav-customers" href="#">Customers</a>
    <a class="nav-tour" href="#">Tour</a>
    <a class="nav-solutions" href="#">Solutions</a>
    <a class="nav-contact" href="#">Contact</a>
  </nav>
  <a class="login" href="#">Login</a>
</header>

<section class="hero">
  <div class="video">
    <div class="video-frame" role="img" aria-label="Chalk drawings of many small light bulbs beside one large bulb on a green chalkboard"></div>
    <svg class="play-big" viewBox="0 0 40 40"><rect width="40" height="40" fill="#000"/><path d="M14 10 L29 20 L14 30Z" fill="#fff"/></svg>
    <div class="controls">
      <svg class="ctrl-play" viewBox="0 0 32 31"><rect width="32" height="31" fill="#5a5a5a"/><path d="M12 9 L22 15.5 L12 22Z" fill="#fff"/></svg>
      <div class="ctrl-track">
        <div class="progress"><span></span></div>
        <div class="knob"></div>
        <div class="time">00.00</div>
      </div>
    </div>
  </div>
  <div class="slide">
    <span class="slide-mark"></span>
    <div class="slide-line l1">Customize</div>
    <div class="slide-line l2">Online Collaboration</div>
    <div class="slide-line l3">Team Work</div>
    <div class="dots"><i></i><i class="on"></i><i></i><i></i><i></i><i></i></div>
  </div>
</section>

<section class="features">
  <article class="feature"><h3>Customize Application</h3><div class="photo photo-apps" role="img" aria-label="Keyboard close-up with blue keys spelling apps"></div></article>
  <article class="feature"><h3>Synchronize All Device</h3><div class="photo photo-servers" role="img" aria-label="Server room aisle between rows of racks"></div></article>
  <article class="feature"><h3>Report</h3><div class="photo photo-report" role="img" aria-label="Printed financial report charts with a pen and calculator"></div></article>
</section>

<nav class="footer-nav"><a href="#">Pricing &amp; Sign up</a><a href="#">Blog</a><a href="#">Support</a><a href="#">Privacy Policy</a><a href="#">Terms</a></nav>
<p class="copyright">©2013 Tallyleaf. All rights reserved.</p>
</body>
</html>
```